Web Design Business Card

I need a new business card designed, we recently rebranded and I need to get a fresh design to match our new logo, colours and branding.

Details:

Dorin Vaskel | Founder & CEO
Address: 7 Fernbrook Lane, #14-05 Maralune Crest, Singapore 318457
Tel: +65 93640281
Web: www.plumtrove.com.sg
hello@plumtrove.com.sg

I've attached my old card as well

Industry/Entity Type

Business

Requirements
Must have
• Front and Back
Interesting use of logo
Correct use of colour scheme

```html
<!DOCTYPE html>
<html lang="en">
<head>
<meta charset="utf-8">
<title>Plumtrove Business Card</title>
<link href="https://fonts.googleapis.com/css2?family=Source+Sans+3:wght@400;600;700&display=swap" rel="stylesheet">
<style>
  :root {
    --page-bg: #d6cdc1;
    --card-bg: #e9e8e3;
    --brand-blue: #1aaeea;
    --brand-brown: #6e625b;
    --rule: #85807a;
    --watermark: #d2e4ea;
    --rail: #dddcd6;
    --white: #ffffff;
  }
  * { margin: 0; padding: 0; box-sizing: border-box; }
  html, body {
    width: 1200px;
    height: 1000px;
    overflow: hidden;
  }
  body {
    position: relative;
    background: var(--page-bg);
    font-family: "Source Sans 3", Arial, sans-serif;
  }
  .card {
    position: absolute;
    background: var(--card-bg);
    overflow: hidden;
  }

  /* Logo side */
  .card-logo-side {
    left: 265px; top: 128px; width: 730px; height: 415px;
  }
  .brand {
    position: absolute;
    display: flex;
    align-items: center;
  }
  .brand-dot {
    border-radius: 50%;
    background: var(--brand-blue);
    flex: none;
  }
  .brand-text { display: flex; flex-direction: column; }
  .brand-name {
    color: var(--brand-brown);
    font-weight: 700;
    line-height: 1;
    letter-spacing: -0.3px;
  }
  .brand-tagline {
    color: var(--brand-blue);
    font-weight: 700;
    text-transform: uppercase;
    letter-spacing: 0.4px;
    white-space: nowrap;
  }
  .card-logo-side .brand { left: 247px; top: 174px; }
  .card-logo-side .brand-dot { width: 66px; height: 66px; margin-right: 12px; }
  .card-logo-side .brand-name { font-size: 42px; }
  .card-logo-side .brand-tagline { font-size: 9.5px; margin-top: 5px; }

  /* Details side */
  .card-details-side {
    left: 167px; top: 497px; width: 728px; height: 416px;
  }
  .watermark-circle {
    position: absolute;
    left: 185px; top: 78px;
    width: 316px; height: 316px;
    border-radius: 50%;
    background: var(--watermark);
  }
  .card-details-side .brand { left: 48px; top: 43px; }
  .card-details-side .brand-dot { width: 41px; height: 41px; margin-right: 8px; }
  .card-details-side .brand-name { font-size: 26px; }
  .card-details-side .brand-tagline { font-size: 6px; margin-top: 2px; }

  .person {
    position: absolute;
    left: 457px; top: 30px;
  }
  .person-name {
    color: var(--brand-blue);
    font-size: 32px;
    font-weight: 700;
    letter-spacing: 1px;
    line-height: 1.1;
    white-space: nowrap;
  }
  .person-role {
    color: var(--brand-brown);
    font-size: 23px;
    line-height: 1.1;
  }
  .header-rule {
    position: absolute;
    left: 0; top: 116px;
    width: 713px; height: 1px;
    background: var(--rule);
  }
  .scroll-rail {
    position: absolute;
    right: 0; top: 0;
    width: 15px; height: 100%;
    background: var(--rail);
    border-left: 1px solid #cfcdc7;
  }
  .scroll-thumb {
    position: absolute;
    left: 717px; top: 38px;
    width: 8px; height: 62px;
    border-radius: 4px;
    background: var(--brand-blue);
  }

  .field { position: absolute; }
  .field-label {
    color: var(--brand-brown);
    font-size: 13px;
    font-weight: 700;
    text-transform: uppercase;
    letter-spacing: 0.2px;
  }
  .field-value {
    position: relative;
    display: inline-block;
    margin-top: 14px;
    background: var(--brand-blue);
    color: var(--white);
    font-size: 16px;
    line-height: 20px;
    padding: 8px 10px 8px 8px;
    white-space: nowrap;
  }
  .field-value::before {
    content: "";
    position: absolute;
    left: 18px; top: -11px;
    border-left: 9px solid transparent;
    border-right: 9px solid transparent;
    border-bottom: 11px solid var(--brand-blue);
  }
  .field-web { left: 47px; top: 163px; }
  .field-email { left: 47px; top: 261px; }
  .field-web .field-value,
  .field-email .field-value { min-width: 179px; }
  .field-contact { left: 460px; top: 163px; }
  .field-contact .field-value { min-width: 165px; padding-left: 12px; letter-spacing: 0.5px; }
  .field-address { left: 460px; top: 261px; }
  .field-address .field-value { min-width: 165px; padding: 7px 10px 8px 11px; line-height: 19.5px; }
</style>
</head>
<body>
  <section class="card card-logo-side" aria-label="Business card, logo side">
    <div class="brand">
      <span class="brand-dot"></span>
      <div class="brand-text">
        <span class="brand-name">plumtrove</span>
        <span class="brand-tagline">Web Design &amp; Consultancy</span>
      </div>
    </div>
  </section>

  <section class="card card-details-side" aria-label="Business card, contact side">
    <div class="watermark-circle"></div>
    <div class="brand">
      <span class="brand-dot"></span>
      <div class="brand-text">
        <span class="brand-name">plumtrove</span>
        <span class="brand-tagline">Web Design &amp; Consultancy</span>
      </div>
    </div>
    <div class="person">
      <div class="person-name">Dorin Vaskel</div>
      <div class="person-role">Founder</div>
    </div>
    <div class="header-rule"></div>
    <div class="scroll-rail"></div>
    <div class="scroll-thumb"></div>

    <div class="field field-web">
      <div class="field-label">Web Site</div>
      <div class="field-value">www.plumtrove.com.sg</div>
    </div>
    <div class="field field-email">
      <div class="field-label">Email</div>
      <div class="field-value">hello@plumtrove.com.sg</div>
    </div>
    <div class="field field-contact">
      <div class="field-label">Contact</div>
      <div class="field-value">+65 9364 0281</div>
    </div>
    <div class="field field-address">
      <div class="field-label">Address</div>
      <div class="field-value">7 Fernbrook Lane,<br>#14-05 Maralune Crest,<br>Singapore 318457</div>
    </div>
  </section>
</body>
</html>
```